Astrologer needs a design for business card

I need a business card design for my job in astrology and flower therapy.
In front side need the information add file.

In back side need the informations above:
INTERPRETAÇÕES
TENDÊNCIAS
AUTOCONHECIMENTO
ANÁLISE VOCACIONAL
DIRECIONAMENTO DE CARREIRA
RELACIONAMENTOS
ASTROLOGIA EMPRESARIAL
TERAPIA FLORAL – Florias de Dorsk e Rui Tavenco

Business

OVRA

```html
<!DOCTYPE html>
<html lang="pt">
<head>
<meta charset="utf-8">
<title>Lirien Sauvo – Cartão de Visita</title>
<link rel="stylesheet" href="https://fonts.googleapis.com/css2?family=Saira+Condensed:wght@400;500&display=swap">
<style>
  :root {
    --stage: #d6d6d4;
    --card: #e9eaea;
    --card-tint: #f1e3d8;
    --accent: #f2681f;
    --accent-soft: #f6b894;
    --shadow: rgba(0,0,0,0.18);
  }
  * { margin: 0; padding: 0; box-sizing: border-box; }
  html, body {
    width: 1200px; height: 900px; overflow: hidden;
    background: var(--stage);
    font-family: "Saira Condensed", "Arial Narrow", sans-serif;
    color: var(--accent);
  }
  .stage { position: relative; width: 1200px; height: 900px; }
  .card {
    position: absolute; left: 260px;
    width: 680px; height: 388px;
    background: var(--card);
    box-shadow: 0 6px 18px var(--shadow);
    overflow: hidden;
  }
  .card--back { top: 44px; }
  .card--front { top: 468px; }
  .card__pattern {
    position: absolute; inset: 0;
    background: radial-gradient(ellipse at 30% 40%, var(--card-tint) 0%, var(--card) 60%),
                radial-gradient(ellipse at 85% 70%, var(--card-tint) 0%, transparent 55%);
    opacity: 0.7;
  }

  /* back side: services list */
  .services {
    position: absolute; left: 96px; top: 48px;
    list-style: none;
    font-family: "Saira Condensed", "Arial Narrow", sans-serif;
    font-weight: 400;
    font-size: 27px; line-height: 34px; letter-spacing: 0.3px;
    text-transform: uppercase;
    white-space: nowrap;
  }
  .services li { position: relative; padding-left: 26px; }
  .services li::before {
    content: ""; position: absolute; left: 2px; top: 12px;
    width: 11px; height: 11px; border-radius: 50%;
    background: var(--accent);
  }
  .services .services__note { text-transform: none; }
  .services .services__note span { text-transform: uppercase; }

  /* front side */
  .identity {
    position: absolute; left: 200px; top: 52px; width: 440px; text-align: center;
  }
  .identity__name {
    font-weight: 500; font-size: 82px; line-height: 1; letter-spacing: 1px;
  }
  .identity__signs {
    display: block; margin: 16px auto 0;
    width: 380px; height: 20px;
    background: var(--accent-soft);
    border-radius: 2px;
  }
  .contact { position: absolute; }
  .contact__rule { display: block; height: 3px; background: var(--accent); }
  .contact__text { font-size: 25px; letter-spacing: 0.5px; }
  .contact--email { left: 34px; top: 222px; width: 300px; }
  .contact--email .contact__icon { position: absolute; left: 118px; top: -34px; }
  .contact--email .contact__text { margin-top: 6px; }
  .contact--phone { right: 34px; top: 286px; width: 300px; }
  .contact--phone .contact__icon { position: absolute; right: 70px; top: -30px; }
  .contact--phone .contact__text { margin-top: 4px; font-size: 34px; letter-spacing: 3px; text-align: right; }
</style>
</head>
<body>
<main class="stage">

  <section class="card card--back" aria-label="Verso do cartão">
    <div class="card__pattern" role="img" aria-label="Símbolos do zodíaco em tom pêssego suave ao fundo"></div>
    <ul class="services">
      <li>Interpretações</li>
      <li>Tendências</li>
      <li>Autoconhecimento</li>
      <li>Análise vocacional</li>
      <li>Direcionamento de carreira</li>
      <li>Relacionamentos</li>
      <li>Astrologia empresarial</li>
      <li class="services__note"><span>Terapia floral</span> – Florias de Dorsk e Rui Tavenco</li>
    </ul>
  </section>

  <section class="card card--front" aria-label="Frente do cartão">
    <div class="card__pattern" role="img" aria-label="Símbolos do zodíaco em tom pêssego suave ao fundo"></div>

    <div class="identity">
      <h1 class="identity__name">Lirien Sauvo</h1>
      <span class="identity__signs" role="img" aria-label="Fileira com os doze signos do zodíaco"></span>
    </div>

    <div class="contact contact--email">
      <svg class="contact__icon" width="40" height="28" viewBox="0 0 40 28" aria-hidden="true">
        <rect x="2" y="2" width="36" height="24" fill="none" stroke="#f2681f" stroke-width="2.5"/>
        <polyline points="2,2 20,16 38,2" fill="none" stroke="#f2681f" stroke-width="2.5"/>
      </svg>
      <span class="contact__rule"></span>
      <p class="contact__text">liriensauvo@correio.net</p>
    </div>

    <div class="contact contact--phone">
      <svg class="contact__icon" width="44" height="24" viewBox="0 0 44 24" aria-hidden="true">
        <rect x="2" y="2" width="40" height="20" rx="4" fill="#f2681f"/>
        <rect x="8" y="5" width="28" height="14" fill="#e9eaea"/>
        <circle cx="39" cy="12" r="1.6" fill="#e9eaea"/>
      </svg>
      <span class="contact__rule"></span>
      <p class="contact__text">(51)9274-3068</p>
    </div>
  </section>

</main>
</body>
</html>
```